Dennis K. Halvorsen stationery and new logo

Create Word template stationery, with a logo, for a Forensic Psychiatry business.

The stationery must include contact info (see below)

The logo should include images similar to (but not necessarily identical to) the ones in the uploaded document. They are the scales of justice and the caduceus, or staff, associated with medicine.

Target Market(s)

consumers of forensic psychiatry (usually lawyers and their clients)

Industry/Entity Type

Mental Health

Logo Text

Dennis K. Halvorsen, MD, DLFAPA

Font styles to use
Serif

Colors

Designer to choose colors to be used in the design.

Requirements
Must have
• Forensic Psychiatry
• 715 N. Maple Street
• R Building
• West Ashford, PA 19804
• (484) 555-3172
Nice to have
• Conservative color scheme

```html
<!DOCTYPE html>
<html lang="en">
<head>
<meta charset="utf-8">
<title>Dennis K. Halvorsen, MD, DLFAPA — Business Card</title>
<link href="https://fonts.googleapis.com/css2?family=Source+Serif+4:wght@400;600&family=Roboto:wght@400;500&display=swap" rel="stylesheet">
<style>
  :root {
    --navy: #132a51;
    --grey-text: #585858;
    --grey-mid: #8a8a8a;
    --grey-band: #a3a3a3;
    --white: #ffffff;
    --backdrop: #ececee;
  }
  * { margin: 0; padding: 0; box-sizing: border-box; }
  html, body {
    width: 1111px;
    height: 1200px;
    overflow: hidden;
    background: var(--backdrop);
  }
  .card {
    position: absolute;
    left: 202px;
    width: 725px;
    height: 404px;
    overflow: hidden;
  }
  .card--front { top: 142px; background: var(--white); }
  .card--back  { top: 631px; background: var(--navy); }

  /* Wordmark: name on top, rule + credentials below, rule fills the remaining width */
  .wordmark {
    position: absolute;
    display: flex;
    flex-direction: column;
    width: max-content;
    font-family: "Source Serif 4", Georgia, serif;
    white-space: nowrap;
  }
  .wordmark__name {
    display: block;
    font-weight: 600;
    line-height: 1;
    letter-spacing: 0.2px;
  }
  .wordmark__row {
    display: flex;
    align-items: center;
  }
  .wordmark__rule {
    flex: 1;
    height: 2px;
  }
  .wordmark__credentials {
    font-weight: 400;
    line-height: 1;
  }

  /* Front wordmark, right aligned */
  .card--front .wordmark { right: 60px; top: 58px; }
  .card--front .wordmark__name { font-size: 35px; color: var(--navy); }
  .card--front .wordmark__row { margin-top: 4px; gap: 9px; }
  .card--front .wordmark__rule { background: var(--grey-mid); margin-top: 6px; }
  .card--front .wordmark__credentials { font-size: 30px; color: var(--grey-mid); }

  /* Back wordmark, centred */
  .card--back .wordmark { left: 50%; transform: translateX(-50%); top: 147px; }
  .card--back .wordmark__name { font-size: 50px; color: var(--white); }
  .card--back .wordmark__row { margin-top: 5px; gap: 12px; }
  .card--back .wordmark__rule { height: 3px; background: var(--white); margin-top: 9px; }
  .card--back .wordmark__credentials { font-size: 44px; color: var(--white); }

  .contact {
    position: absolute;
    left: 61px; top: 221px;
    font-family: "Roboto", Arial, sans-serif;
    font-size: 18px;
    line-height: 22.5px;
    color: var(--grey-text);
  }
  .contact__specialty { color: var(--navy); font-weight: 500; }
  .contact__lines { margin-bottom: 4px; }
  .contact__item { display: flex; align-items: center; gap: 6px; line-height: 24px; }
  .contact__icon { width: 17px; height: 14px; flex: none; fill: var(--navy); }

  .accent-band {
    position: absolute;
    left: 0; bottom: 0;
    width: 725px; height: 11px;
  }
</style>
</head>
<body>

<section class="card card--front">
  <div class="wordmark">
    <span class="wordmark__name">Dennis K. Halvorsen,</span>
    <div class="wordmark__row">
      <span class="wordmark__rule"></span>
      <span class="wordmark__credentials">MD, DLFAPA</span>
    </div>
  </div>

  <div class="contact">
    <div class="contact__specialty">Forensic Psychiatry</div>
    <div class="contact__lines">
      715 N. Maple Street<br>
      R Building West Ashford, PA 19804
    </div>
    <div class="contact__item">
      <svg class="contact__icon" viewBox="0 0 17 14" aria-hidden="true">
        <path d="M0 4.5 C2 1 15 1 17 4.5 L17 6 L13 6 L12.5 4 C10 3.4 7 3.4 4.5 4 L4 6 L0 6 Z"/>
        <path d="M4 7 L13 7 L15 13.5 L2 13.5 Z"/>
      </svg>
      <span>(484) 555-3172</span>
    </div>
    <div class="contact__item">
      <svg class="contact__icon" viewBox="0 0 17 14" aria-hidden="true">
        <path d="M0 2 H17 V13 H0 Z"/>
        <path d="M1 3 L8.5 8.8 L16 3 V4.4 L8.5 10.2 L1 4.4 Z" fill="var(--white)"/>
        <path d="M1 12.2 L6.2 7.6 L7 8.3 L2.2 12.6 Z M16 12.2 L10.8 7.6 L10 8.3 L14.8 12.6 Z" fill="var(--white)"/>
      </svg>
      <span>info@youremail.com</span>
    </div>
  </div>

  <svg class="accent-band" viewBox="0 0 725 11" preserveAspectRatio="none" aria-hidden="true">
    <polygon points="0,0 366,0 357,11 0,11" fill="var(--navy)"/>
    <polygon points="372,0 725,0 725,11 362,11" fill="var(--grey-band)"/>
  </svg>
</section>

<section class="card card--back">
  <div class="wordmark">
    <span class="wordmark__name">Dennis K. Halvorsen,</span>
    <div class="wordmark__row">
      <span class="wordmark__rule"></span>
      <span class="wordmark__credentials">MD, DLFAPA</span>
    </div>
  </div>
</section>

</body>
</html>
```